Plakat-Design für eine Werbeschild für ein Geflügelhof
Zielgruppe
Wir sind ein Geflügelhof, Landhandel, Hofladen, Eier stehen seit über 100 Jahren für Hof Kranwede, artgerechte Tierhaltung und Artikelvielfalt machen uns bekannt.
Aufgabenstellung
Das Werbeschild wird auf dem Hof aufgestellt und soll den Weg zum Hof zeigen.
- die Maße vom Schild: 1,50m breit x 2,40m hoch
- Grafiken werden als .ai und .pdf benötigt
- Logo ist hochgelagen
- Foto von unserer Vorstellung ist hochgeladen
Das Schild muss 400 m RECHTS drauf gedruckt haben.
Falls es zu breit wäre, könnte das Logo ja vielleicht auch über Hof Kranwede.
Das ganze wird bei plattenwerk auf eine MetoxPan-Platte in den Druck gegeben.

```html
<!DOCTYPE html>
<html lang="de">
<head>
<meta charset="utf-8">
<title>Hof Kranwede – Einkauf auf dem Bauernhof</title>
<link rel="stylesheet" href="https://fonts.googleapis.com/css2?family=Varela+Round&family=Open+Sans:wght@700&display=swap">
<style>
  :root {
    --sky-top: #5e2a8a;
    --sky-magenta: #b8378f;
    --sky-rose: #e04f6a;
    --sun-orange: #f07c2c;
    --sun-gold: #f6a624;
    --meadow: #b9b52c;
    --meadow-dark: #6f7f26;
    --white: #ffffff;
    --sign-green: #1e7a36;
  }
  html, body {
    margin: 0;
    padding: 0;
    overflow: hidden;
    background: #ffffff;
  }
  .sign {
    position: relative;
    width: 750px;
    height: 1200px;
    overflow: hidden;
    font-family: "Varela Round", sans-serif;
  }
  .sign__scene {
    position: absolute;
    inset: 0;
    width: 750px;
    height: 1200px;
  }
  .brand {
    position: absolute;
    left: 30px;
    top: 38px;
    display: flex;
    align-items: center;
    gap: 22px;
  }
  .brand__mark {
    width: 118px;
    height: 118px;
    border-radius: 50%;
    border: 5px solid var(--white);
    box-sizing: border-box;
  }
  .brand__name {
    color: var(--white);
    font-size: 60px;
    line-height: 1;
    white-space: nowrap;
  }
  .headline {
    position: absolute;
    left: 0;
    right: 0;
    top: 262px;
    margin: 0;
    text-align: center;
    color: var(--white);
    font-weight: 400;
    line-height: 1;
  }
  .headline__big {
    display: block;
    font-size: 118px;
    letter-spacing: 1px;
  }
  .headline__small {
    display: block;
    font-size: 52px;
    margin: 8px 0 12px;
  }
  .direction {
    position: absolute;
    left: 45px;
    top: 925px;
    width: 665px;
    height: 210px;
  }
  .direction__arrow {
    position: absolute;
    inset: 0;
  }
  .direction__text {
    position: absolute;
    left: 20px;
    top: 55px;
    height: 105px;
    display: flex;
    align-items: center;
    font-family: "Open Sans", sans-serif;
    font-weight: 700;
    font-size: 64px;
    color: var(--sign-green);
    white-space: nowrap;
    letter-spacing: -0.5px;
  }
</style>
</head>
<body>
  <main class="sign">
    <svg class="sign__scene" viewBox="0 0 750 1200" role="img" aria-label="Illustrierte Landschaft bei Sonnenaufgang mit Tannen, Hügeln und Wiese">
      <defs>
        <linearGradient id="sceneGradient" x1="0" y1="0" x2="0" y2="1">
          <stop offset="0" stop-color="var(--sky-top)"/>
          <stop offset="0.2" stop-color="var(--sky-magenta)"/>
          <stop offset="0.38" stop-color="var(--sky-rose)"/>
          <stop offset="0.52" stop-color="var(--sun-orange)"/>
          <stop offset="0.64" stop-color="var(--sun-gold)"/>
          <stop offset="0.76" stop-color="var(--meadow)"/>
          <stop offset="1" stop-color="var(--meadow-dark)"/>
        </linearGradient>
      </defs>
      <rect width="750" height="1200" fill="url(#sceneGradient)"/>
    </svg>

    <header class="brand">
      <div class="brand__mark"></div>
      <div class="brand__name">Hof Kranwede</div>
    </header>

    <h1 class="headline">
      <span class="headline__big">Einkauf</span>
      <span class="headline__small">auf dem</span>
      <span class="headline__big">Bauernhof</span>
    </h1>

    <div class="direction">
      <svg class="direction__arrow" viewBox="0 0 665 210" aria-hidden="true">
        <polygon points="0,55 560,55 560,0 665,105 560,210 560,160 0,160" fill="var(--white)"/>
      </svg>
      <div class="direction__text">in 400m rechts</div>
    </div>
  </main>
</body>
</html>
```